120ml Jar Label — Masculine Cosmetic Foot Balm for Cracked, Hardworking Heels

We need a print-ready wraparound label for a 120ml jar — a brown/amber glass jar with a black metal screw lid (file photo attached).

--DO NOT PUT A BARCODE ON THE LABEL PLEASE--
**PLEASE READ "PLAN HUDDLE PROJECT BRIEF FINAL.MD" IN ATTACHED FILES IF YOU ARE SUBMITTING A DESIGN.**

The label is 190mm wide × 40mm high.
We need files to be in an .ai format with a 2mm bleed at the end.
Social media handle: @bramblekeepnz (facebook, instagram and tiktok)

Bramble Keep is a New Zealand foot-care brand making practical, no-nonsense products for hardworking men whose jobs wreck their feet. Our flagship product, Ridge Mender Balm, helps fix thick, cracked, hardworking skin.

Brand color scheme and overview is all in the brief file. You may add some brand aligned colors outside of the specified hex codes as you see fit to make a great design. Feel free to remove the "Bramble Keep" text from the logo so Bramble Keep is not doubled up on the front of the label

The tone we want: direct, rugged, and credible — like a workwear brand, not a spa brand. Most cracked-heel products on the market lean soft and feminine; we want to stand apart by looking like a serious fix for a real problem, made in New Zealand.

Full legal requirements for New Zealand cosmetic labelling (ingredients, directions, net contents, origin, etc.) are listed in the attached brief document — these are non-negotiable and must stay legible.

Please see the label attached "Label spacing guide" for this project's rough spacing guide. This label is the same size and sits well on the jar. This label doesn't need to be spaced quite as much as the Verin Label

I want to run the design for a week - I feel 7 days is a good amount of time for designers to see the work, digest the brief and create something remarkable and memorable for Bramble Keep.

Target Market(s)

Working men in New Zealand whose jobs or lifestyle put heavy wear on their feet — tradies, farmers, hospital/shift workers, hunters, and outdoors people. Practical, value-driven buyers rather than luxury skincare shoppers.

Industry/Entity Type

Beauty / Health & Wellness / Cosmetics

Font styles to use
Sans Serif
Other font styles liked:
• Montserrat (bold, headings), Inter (regular, body)

Colors
00AB8E
00BBA5
67D7C9
C6EFE9
E9F9F6
FFC000
F8CF3A
FAE287
FDF2CF
FEFAEE

Requirements
Must have
• All NZ cosmetic labelling requirements from the attached brief (product name, tag line, net contents, ingredients, directions, storage, made in NZ) — legible and complete, not omitted for aesthetics Fits 190mm × 40mm wraparound format for a 120ml brown jar with black lid Uses our existing brand colors: Deep Olive #3C4A34, Bone White #F4EFE6, Terracotta Clay #C1683D, and Warm Grey #4A4540 (exact palette in attached brief) Uses Montserrat (headings) and Inter (body) or close equivalents Incorporates our existing shield-and-wing logo (attached) Brand name and product name clearly readable from a normal shelf/bathroom-cabinet distance
Nice to have
• A style that could extend into a hero/product photo later, similar to the NZ-hills-backdrop look on our website (screenshot attached) — not required for the label itself, just good to keep in mind Original icon work (e.g. a small soak/apply/sock icon set) if it fits the rugged brand feel A design that could work as a small back-label/wraparound split if the front can't fit everything at a readable size
Should not have
• No pastel colors, floral motifs, or delicate script fonts — this should never look like spa/luxury skincare. Don't introduce new brand colors outside the palette provided other than black.

```html
<!DOCTYPE html>
<html lang="en">
<head>
<meta charset="utf-8">
<title>Bramble Keep — Ridge Mender Balm Jar Label</title>
<link rel="stylesheet" href="https://fonts.googleapis.com/css2?family=Montserrat:wght@300;400;600;700&display=swap">
<style>
  :root {
    --paper: #ffffff;
    --forest: #132b20;
    --fern-shade: #0f231a;
    --silver: #cbc8bf;
    --silver-soft: #b9b5ab;
    --icon-fill: #2a4036;
    --trim-red: #c8332a;
  }
  * { margin: 0; padding: 0; box-sizing: border-box; }
  html, body { width: 1200px; height: 1200px; overflow: hidden; background: var(--paper); }
  body { position: relative; font-family: "Montserrat", sans-serif; color: var(--silver); }

  .label { position: absolute; background: var(--forest); overflow: hidden; }
  .label-front { left: 291px; top: 199px; width: 631px; height: 403px; overflow: visible; }
  .label-wrap { left: 121px; top: 780px; width: 975px; height: 241px; }

  .trim-line { position: absolute; height: 1px; background: var(--trim-red); }
  .trim-frame { position: absolute; left: 9px; top: 10px; right: 10px; bottom: 10px; border: 1px solid var(--trim-red); }

  .fern-decor { position: absolute; background: var(--fern-shade); opacity: .8; border-radius: 50% 50% 45% 45%; }

  .wordmark { position: absolute; font-family: "Montserrat", sans-serif; font-weight: 700; color: var(--silver); line-height: .92; letter-spacing: -1px; white-space: nowrap; }
  .wordmark .wordmark-suffix { font-size: .42em; letter-spacing: 0; }
  .mark-square { position: absolute; background: var(--icon-fill); border: 2px solid var(--silver); }

  .product-name { position: absolute; font-weight: 700; color: var(--silver-soft); text-align: center; white-space: nowrap; transform: translateX(-50%); }
  .origin-line { position: absolute; font-weight: 400; color: var(--silver-soft); white-space: nowrap; transform: translateX(-50%); }

  .info-copy { position: absolute; left: 30px; top: 20px; width: 210px; font-size: 8.6px; line-height: 11.2px; font-weight: 400; color: var(--silver); }
  .info-copy p { margin-bottom: 1px; }
  .info-heading { font-weight: 700; font-size: 11px; letter-spacing: .3px; margin-right: 6px; }

  .badge { position: absolute; width: 72px; text-align: center; transform: translateX(-50%); }
  .badge-title { height: 14px; display: flex; align-items: flex-end; justify-content: center; font-size: 5px; line-height: 6px; letter-spacing: .3px; text-transform: uppercase; margin-bottom: 4px; }
  .badge-icon { display: block; margin: 0 auto; width: 30px; height: 30px; border-radius: 50%; background: var(--icon-fill); border: 1px solid var(--silver-soft); }

  .social-handle { position: absolute; left: 784px; top: 99px; display: flex; align-items: center; gap: 6px; font-weight: 700; font-size: 11.5px; }
  .social-dot { width: 16px; height: 16px; border-radius: 50%; background: var(--silver); }
  .web-address { position: absolute; left: 841px; top: 122px; transform: translateX(-50%); font-weight: 700; font-size: 11.5px; white-space: nowrap; }
  .tagline { position: absolute; left: 841px; top: 178px; transform: translateX(-50%); text-align: center; font-weight: 700; font-size: 11px; line-height: 15px; letter-spacing: .6px; }
  .net-contents { position: absolute; left: 937px; top: 198px; transform: translate(-50%, -50%) rotate(-90deg); font-weight: 400; font-size: 14px; letter-spacing: .5px; }
</style>
</head>
<body>

  <section class="label label-front">
    <div class="trim-line" style="left:-4px; top:10px; width:635px;"></div>
    <div class="trim-line" style="left:-4px; top:391px; width:635px;"></div>

    <div class="fern-decor" role="img" aria-label="Faint silver fern frond rising on the left" style="left:0; top:105px; width:230px; height:260px;"></div>
    <div class="fern-decor" role="img" aria-label="Faint silver fern frond rising on the right" style="left:400px; top:105px; width:231px; height:260px;"></div>

    <div class="mark-square" style="left:60px; top:90px; width:150px; height:150px;"></div>

    <div class="wordmark" style="left:275px; top:92px; font-size:74px;">Bramble<br>Keep <span class="wordmark-suffix">NZ</span></div>

    <div class="product-name" style="left:315px; top:308px; font-size:33px;">Ridge Mender Balm</div>
    <div class="origin-line" style="left:315px; top:360px; font-size:14px;">Made In New Zealand</div>
  </section>

  <section class="label label-wrap">
    <div class="trim-frame"></div>

    <div class="fern-decor" role="img" aria-label="Faint silver fern frond on the left of centre" style="left:250px; top:20px; width:170px; height:200px;"></div>
    <div class="fern-decor" role="img" aria-label="Faint silver fern frond on the right of centre" style="left:560px; top:20px; width:170px; height:200px;"></div>

    <div class="info-copy">
      <p><span class="info-heading">DIRECTIONS:</span>Apply generously to clean, dry feet, focusing on heels and thick or cracked areas. For cracked heels, wear our moisture-locking socks overnight. Use daily.</p>
      <p><span class="info-heading">INGREDIENTS:</span>Shea Butter, Beef Tallow, Beeswax, Grape Seed Oil, Vegetable Glycerin, Lanolin, Panthenol, Gluconolactone, Sodium Benzoate, Allantoin, Manuka Honey, Vitamin E, Tea Tree Essential Oil, Lemon Myrtle Essential Oil, Rosemary Oleoresin Extract</p>
      <p><span class="info-heading">STORAGE:</span>Keep out of direct sunlight. Best used within six months of opening.</p>
    </div>

    <div class="badge" style="left:50px; top:160px;"><div class="badge-title">Hand-made</div><span class="badge-icon" role="img" aria-label="Hand-made icon"></span></div>
    <div class="badge" style="left:133px; top:160px;"><div class="badge-title">Hydrating</div><span class="badge-icon" role="img" aria-label="Hydrating droplets icon"></span></div>
    <div class="badge" style="left:210px; top:160px;"><div class="badge-title">Not tested<br>on animals</div><span class="badge-icon" role="img" aria-label="Not tested on animals icon"></span></div>

    <div class="mark-square" style="left:340px; top:52px; width:100px; height:100px;"></div>
    <div class="wordmark" style="left:460px; top:65px; font-size:40px;">Bramble<br>Keep <span class="wordmark-suffix">NZ</span></div>

    <div class="product-name" style="left:486px; top:182px; font-size:21px;">Ridge Mender Balm</div>
    <div class="origin-line" style="left:486px; top:213px; font-size:9px;">Made In New Zealand</div>

    <div class="badge" style="left:768px; top:28px;"><div class="badge-title">For all<br>skin types</div><span class="badge-icon" role="img" aria-label="All skin types icon"></span></div>
    <div class="badge" style="left:838px; top:28px;"><div class="badge-title">100% natural<br>ingredients</div><span class="badge-icon" role="img" aria-label="Natural ingredients icon"></span></div>
    <div class="badge" style="left:908px; top:28px;"><div class="badge-title">Made in<br>New Zealand</div><span class="badge-icon" role="img" aria-label="New Zealand outline icon"></span></div>

    <div class="social-handle"><span class="social-dot"></span>@bramblekeep</div>
    <div class="web-address">www.bramblekeep.co.nz</div>

    <div class="tagline">FOR<br>HARDWORKING<br>SOLES</div>
    <div class="net-contents">100ML</div>
  </section>

</body>
</html>
```